International Supplement Company Requires Re-design of Product Label

We are a company that manufactures and sells Nutritional Supplements. We have a wide range of products suitable for all different health needs; sports, wellbeing, weight-loss, ailments. The label needs to be suitable for all varieties of product.
We are looking to update our current supplement bottle labels to make our products appear more attractive and eye catching. We find our current label boring and it doesn’t stand out well when mixed with other competitor products on sites such as Brellix and Tundro.
We use flat postal pack bottles which are postal friendly and fit through a letterbox. Our product bottles contain a front and a back label. The bottles can be seen on our website – www.corvantia.co.uk. It is the label on the front of our bottle which we require re-designing. The back contains all of the ingredients, directions, expiry, company info etc and is therefore font only and can be easily designed and laid out by us.
We have two sizes of labels – the first is 66mm by 86mm in size and the second is 86mm by 150mm. The design has to be transferrable from one size to the other.
We are looking for a design that is eye catching, memorable and which reflects quality and trust. We would like a clean, straight look with good strong colours. Our products are sold in shops and over the internet. The label design therefore needs to make our product stand out whether on a shop shelf, on a website or on a flyer.
Most of our products are unisex and not therefore targeted at any particular gender. We do however find that our range of sports supplements is purchased more predominantly by males and could therefore stand a slight variation in colour perhaps to make it a little more masculine.
We would like the range of sports supplements to stand out from the other products and would therefore ask that a slight variation be considered for this. We have considered using a darker colours and/or background on the sports range.
The product titles can vary immensely and have a different amount of characters and numbers in each. Some have very short titles (such as ‘Zinc’) whilst others have longer titles (such as ‘Glucosamine 500mg, Chondroitin 100mg & MSM 100mg’). This is something that needs to be considered when designing the area for the title.
The label needs to contain the following information: Product Title; Product Strength (ie mg); GMP logo; Company Logo; Quantity. Please note that some products, when containing more than one ingredient, have the strength written in their title and not listed separately. Please have a look at the different listings on our website to obtain an understanding of this – www.corvantia.co.uk.
We have also considered the use of an image on some of our bottle labels, to depict the main ingredient contained within the product. Not all of the products lend themselves to using an image but some do. Please have a look at some of our competitor labels and see how they use images within their design – www.quillmora.co.uk www.darbelo.co.uk . Products such as Vitamin B Complex and Glucosamine would not lend themselves to having an image but products such as African Mango and Garlic would. We would be happy to source and apply our own images if you choose to produce a design which leaves a space for the image. We believe that the use of an image can sometimes help the product stand out from competitors and can make it more easily identifiable to some customers.
We require the logo to be produced and provided to us in a High Resolution PSD file with editable Layers
Industry/Entity Type
It Company
Logo Text
Corvantia Health & Fitness
Look and feel

```html
<!DOCTYPE html>
<html lang="en">
<head>
<meta charset="utf-8">
<title>Corvantia Front Labels</title>
<link rel="stylesheet" href="https://fonts.googleapis.com/css2?family=Figtree:wght@300;400;700&display=swap">
<style>
  :root {
    --page: #ffffff;
    --label-black: #000000;
    --brand-yellow: #ffec00;
    --text-white: #ffffff;
    --text-grey: #9a9a9a;
    --acai-light: #6e6a78;
    --acai-dark: #1d1b22;
    --rasp-light: #e0405f;
    --rasp-dark: #9c1230;
  }
  * { box-sizing: border-box; margin: 0; padding: 0; }
  html, body {
    width: 1200px;
    height: 890px;
    overflow: hidden;
    background: var(--page);
  }
  .sheet {
    position: relative;
    width: 1200px;
    height: 890px;
  }
  .label {
    position: absolute;
    top: 103px;
    width: 405px;
    height: 703px;
    background: var(--label-black);
    overflow: hidden;
    font-family: "Figtree", Arial, sans-serif;
    text-align: center;
  }
  .label--acai { left: 180px; }
  .label--raspberry { left: 615px; }

  .ingredient-photo {
    position: absolute;
    left: 0;
    top: 0;
    width: 100%;
    height: 560px;
  }
  .label--acai .ingredient-photo {
    background:
      linear-gradient(to bottom, rgba(0,0,0,0) 60%, var(--label-black) 100%),
      radial-gradient(circle at 40% 35%, var(--acai-light), var(--acai-dark) 80%);
  }
  .label--raspberry .ingredient-photo {
    background:
      linear-gradient(to bottom, rgba(0,0,0,0) 60%, var(--label-black) 100%),
      radial-gradient(circle at 45% 35%, var(--rasp-light), var(--rasp-dark) 85%);
  }

  .brand-name {
    position: absolute;
    left: 0;
    right: 0;
    top: 250px;
    color: var(--brand-yellow);
    font-weight: 700;
    font-size: 74px;
    letter-spacing: -1px;
    line-height: 1;
  }

  .purity {
    position: absolute;
    left: 0;
    right: 0;
    top: 524px;
    color: var(--text-white);
    font-weight: 700;
    font-size: 43px;
    line-height: 1;
  }
  .product-title {
    position: absolute;
    left: 0;
    right: 0;
    top: 570px;
    color: var(--brand-yellow);
    font-weight: 300;
    font-size: 60px;
    line-height: 1;
    letter-spacing: 0.5px;
  }
  .strength {
    position: absolute;
    left: 0;
    right: 0;
    top: 645px;
    color: var(--text-white);
    font-weight: 700;
    font-size: 15px;
  }
  .storage-note {
    position: absolute;
    left: 0;
    right: 0;
    top: 679px;
    color: var(--text-grey);
    font-weight: 400;
    font-size: 11.5px;
  }
</style>
</head>
<body>
<main class="sheet">
  <section class="label label--acai">
    <div class="ingredient-photo" role="img" aria-label="Close-up photograph of dark acai berries"></div>
    <p class="brand-name">Corvantia</p>
    <p class="purity">100% PURE</p>
    <h2 class="product-title">ACAI BERRY</h2>
    <p class="strength">Food supplement - 700mg</p>
    <p class="storage-note">For best before date and storage information, see reverse label</p>
  </section>

  <section class="label label--raspberry">
    <div class="ingredient-photo" role="img" aria-label="Close-up photograph of fresh red raspberries"></div>
    <p class="brand-name">Corvantia</p>
    <p class="purity">100% PURE</p>
    <h2 class="product-title">RASPBERRY</h2>
    <p class="strength">Food supplement - 700mg</p>
    <p class="storage-note">For best before date and storage information, see reverse label</p>
  </section>
</main>
</body>
</html>
```